Christmas Flyer for Suburban London Cocktail Bar & Party Venue

We need a flyer with details of our Christmas Party drinks packages for party bookings. Tin and Thistle is a local cocktail bar with an emphasis on providing a modern hospitality environment with a sense of fun and whimsy. We pride ourselves on not being generic, providing a community atmosphere and don't take ourselves too seriously and our brand reflects that.

Christmas is one of the most popular times of year and we host parties for many people in our local area. The flyer is intended to summarise our promotional deals and will be distributed to local businesses as well as being available in the bar for customers.

An overview of our mood board that influences 'tone', as we await rebranding, can be seen at https://au.pinboardia.com/korvelmidge/commercial-bar-fit-out-inspiration/

Target Market(s)

21-35 Urban Professionals

Industry/Entity Type

Hospitality

Colors

Designer to choose colors to be used in the design.

Requirements
Must have
• The 4 offers contained in the copy text. Can be adjusted for legibility as long as the offers remain substantively the same.
• The logo of the bar. The standard logo is the gold version however that can be recoloured if appropriate.
• The Address Tin & Thistle - 27 Wrenmoor Rise - Balham, SW7 4KD - This need not be prominent.
Nice to have
• Our social media locations
• Friendwall /tinandthistlebar
• Snapgram /tinandthistlebar
Should not have
• Should not contain photographs or exceptionally generic stock imagery.

```html
<!DOCTYPE html>
<html lang="en">
<head>
<meta charset="utf-8">
<title>Tin &amp; Thistle – Christmas Drinks Packages</title>
<link rel="stylesheet" href="https://fonts.googleapis.com/css2?family=Francois+One&family=Roboto:wght@300;400&display=swap">
<style>
  :root {
    --navy-deep: #0f2540;
    --navy-mid: #1a3d63;
    --navy-glow: #2f6aa0;
    --side-dark: #123052;
    --side-light: #2a5f8f;
    --gold: #c9aa6c;
    --gold-soft: #d8bd84;
    --white: #f3f6fa;
  }
  * { margin: 0; padding: 0; box-sizing: border-box; }
  html, body { width: 927px; height: 1200px; overflow: hidden; }
  body {
    position: relative;
    background: var(--navy-deep);
    font-family: "Roboto", Arial, sans-serif;
    color: var(--white);
  }
  .side-art {
    position: absolute;
    top: 0;
    width: 184px;
    height: 1200px;
  }
  .side-art--left {
    left: 0;
    background: linear-gradient(170deg, var(--side-dark) 0%, var(--navy-mid) 55%, var(--side-light) 100%);
  }
  .side-art--right {
    right: 0;
    width: 183px;
    background: linear-gradient(190deg, var(--side-dark) 0%, var(--navy-mid) 55%, var(--side-light) 100%);
  }
  .menu-panel {
    position: absolute;
    left: 184px;
    top: 0;
    width: 560px;
    height: 1200px;
    background:
      radial-gradient(ellipse 260px 330px at 50% 48%, rgba(60,130,190,0.55), rgba(60,130,190,0) 100%),
      linear-gradient(180deg, #0e2038 0%, #173556 55%, #1d4a74 100%);
  }
  .brand {
    position: absolute;
    left: 184px;
    width: 560px;
    top: 88px;
    text-align: center;
    font-family: "Francois One", "Arial Narrow", sans-serif;
    font-size: 62px;
    line-height: 70px;
    color: var(--gold);
  }
  .divider {
    position: absolute;
    left: 380px;
    width: 168px;
    height: 40px;
    background: linear-gradient(90deg, rgba(201,170,108,0), rgba(201,170,108,0.35), rgba(201,170,108,0));
    border-radius: 20px;
  }
  .divider--top { top: 238px; }
  .divider--bottom { top: 1022px; height: 48px; }
  .offer {
    position: absolute;
    left: 302px;
    width: 380px;
  }
  .offer__title {
    font-family: "Francois One", "Arial Narrow", sans-serif;
    font-size: 24px;
    line-height: 30px;
    color: var(--gold);
  }
  .offer__items { list-style: none; }
  .offer__items li {
    position: relative;
    padding-left: 21px;
    font-size: 18px;
    font-weight: 300;
    line-height: 23.5px;
  }
  .offer__items li::before {
    content: "\2736";
    position: absolute;
    left: 0;
    top: 0;
    font-size: 14px;
  }
  .offer__price {
    margin-top: 4px;
    padding-left: 21px;
    font-size: 18px;
    line-height: 24px;
    color: var(--gold-soft);
  }
  .offer__price--bold { font-weight: 400; }
  .contact {
    position: absolute;
    left: 184px;
    width: 560px;
    top: 1079px;
    text-align: center;
    font-size: 14.5px;
    font-weight: 300;
    line-height: 19px;
    color: var(--gold-soft);
  }
  .contact__phone svg { vertical-align: -2px; margin-right: 3px; }
  .socials {
    position: absolute;
    left: 356px;
    top: 1131px;
    list-style: none;
    font-size: 14.5px;
    font-weight: 300;
    color: var(--gold-soft);
  }
  .socials li { display: flex; align-items: center; height: 20px; }
  .socials .dot {
    width: 16px; height: 16px; border-radius: 50%;
    background: var(--white);
    margin-right: 8px;
  }
</style>
</head>
<body>
  <div class="side-art side-art--left" role="img" aria-label="Decorative line-art leaves with hanging snowflake baubles and gold sparkles"></div>
  <div class="side-art side-art--right" role="img" aria-label="Decorative line-art leaves with hanging snowflake baubles and gold sparkles"></div>
  <div class="menu-panel"></div>

  <div class="brand">Tin &amp; Thistle</div>
  <div class="divider divider--top" role="img" aria-label="Gold flourish with two leaping reindeer"></div>

  <section class="offer" style="top:293px">
    <h2 class="offer__title">Sharing Combo</h2>
    <ul class="offer__items">
      <li>3 of our sharing cocktails</li>
      <li>Bottle of Prosecco</li>
    </ul>
    <p class="offer__price">£85 / Save up to £35</p>
  </section>

  <section class="offer" style="top:407px">
    <h2 class="offer__title">Xmas Package 1 - 10 People</h2>
    <ul class="offer__items">
      <li>10x Cocktails</li>
      <li>10x Beers</li>
      <li>10x house spirit + mixer, glass<br>of wine or prosecco</li>
      <li>Bottle of prosecco</li>
    </ul>
    <p class="offer__price">£150 / Save up to £65</p>
  </section>

  <section class="offer" style="top:593px">
    <h2 class="offer__title">Xmas Package 2 - 15 People</h2>
    <ul class="offer__items">
      <li>15x Cocktails</li>
      <li>15x Beers</li>
      <li>15x house spirit + mixer, glass<br>of wine or prosecco</li>
      <li>Sharing cocktail</li>
    </ul>
    <p class="offer__price offer__price--bold">£220 / Save up to £85</p>
  </section>

  <section class="offer" style="top:778px">
    <h2 class="offer__title">Xmas Package 3 - 20 People</h2>
    <ul class="offer__items">
      <li>20x Cocktails</li>
      <li>20x Beers</li>
      <li>20x house spirit + mixer, glass<br>of wine or prosecco</li>
      <li>Bottle of prosecco</li>
      <li>Treasure chest! (12 Person Sharer<br>valued at £100)</li>
    </ul>
    <p class="offer__price">£350 / Save up to £150</p>
  </section>

  <div class="divider divider--bottom" role="img" aria-label="Gold flourish with two leaping reindeer"></div>

  <address class="contact" style="font-style:normal">
    27 Wrenmoor Rise - Balham, SW7 4KD<br>
    <span class="contact__phone"><svg width="12" height="12" viewBox="0 0 12 12"><circle cx="6" cy="6" r="5.4" fill="none" stroke="#d8bd84" stroke-width="0.9"/><path d="M4 3.2c-.6.5-.7 1.6.2 2.9s2 2.2 2.9 2.3c.6.1 1-.3 1.2-.7l-1-.8-.6.5c-.5-.2-1.4-1.1-1.6-1.6l.5-.6-.8-1z" fill="#d8bd84"/></svg>020 7946 0321</span>
  </address>

  <ul class="socials">
    <li><span class="dot"></span>Friendwall /tinandthistlebar</li>
    <li><span class="dot"></span>Snapgram /tinandthistlebar</li>
  </ul>
</body>
</html>
```